New career and executive coaching business needs a business card design including logo

Company name: 'Harbourline Career Partners.' The aim of my coaching engagements is to help people improve their communication in the workplace and achieve their career goals. The process involves working with individuals to help them uncover their strengths and talents, then leverage those to improve their working lives. The Tellwood Inventory is the starting point to the process. I am after an exciting and interesting business card design (including logo)which is professional yet will still get people's attention.

Industry/Entity Type

Business

Contact Information for Business Card

Name: Gavin Holloway
Position: Owner
Address: 58 Pellimore Cres, Wardell Vic 3197
Phone: 0481937145
Website: harbourlinecareer.com.au
Email: gavin@hcp.com.au

Colors
33a6d7
00a990
0355a3
3176b5

Requirements
Must have
• logo

```html
<!DOCTYPE html>
<html lang="en">
<head>
<meta charset="utf-8">
<title>Harbourline Career Partners – Business Card</title>
<link rel="stylesheet" href="https://fonts.googleapis.com/css2?family=Roboto:wght@400;500;700&display=swap">
<style>
  :root {
    --page-bg: #ffffff;
    --card-bg: #e6e7e8;
    --sky-blue: #00aeef;
    --deep-blue: #1a75bb;
    --icon-blue: #0f6db3;
    --name-blue: #1a6fb5;
    --mark-blue: #1d8fd6;
    --faint-mark: #8fa9d6;
  }
  * { box-sizing: border-box; margin: 0; padding: 0; }
  html, body {
    width: 1200px;
    height: 900px;
    overflow: hidden;
    background: var(--page-bg);
    font-family: "Roboto", Arial, sans-serif;
  }
  .card-set {
    position: absolute;
    left: 70px;
    top: 307px;
    display: flex;
    gap: 60px;
  }
  .card {
    position: relative;
    width: 500px;
    height: 286px;
    background: var(--card-bg);
  }
  .card__band {
    position: absolute;
    left: 0;
    width: 100%;
    height: 14px;
    display: flex;
  }
  .card__band--top { top: 0; }
  .card__band--bottom { bottom: 0; }
  .card__band span { flex: 1; }
  .card__band .band-light { background: var(--sky-blue); }
  .card__band .band-dark { background: var(--deep-blue); }

  /* Front */
  .brand-lockup {
    position: absolute;
    left: 0;
    right: 0;
    top: 96px;
    display: flex;
    align-items: center;
    justify-content: center;
    gap: 12px;
  }
  .brand-lockup__dot {
    width: 44px;
    height: 44px;
    border-radius: 50%;
    background: var(--sky-blue);
  }
  .brand-lockup__name {
    font-size: 24px;
    font-weight: 700;
    color: var(--mark-blue);
    line-height: 1.1;
  }
  .website {
    position: absolute;
    left: 0;
    right: 0;
    top: 236px;
    text-align: center;
    font-size: 14px;
    font-weight: 500;
    letter-spacing: 2.6px;
    color: var(--deep-blue);
  }

  /* Back */
  .person {
    position: absolute;
    right: 28px;
    top: 52px;
    text-align: right;
  }
  .person__name {
    font-size: 21px;
    font-weight: 700;
    color: var(--name-blue);
    letter-spacing: -0.2px;
  }
  .person__role {
    font-size: 10px;
    font-weight: 500;
    letter-spacing: 1.4px;
    color: var(--sky-blue);
  }
  .contact-list {
    position: absolute;
    left: 56px;
    top: 131px;
    list-style: none;
  }
  .contact-list li {
    display: flex;
    align-items: center;
    gap: 14px;
    height: 28px;
    margin-bottom: 12px;
    font-size: 11px;
    font-weight: 700;
    color: var(--sky-blue);
  }
  .contact-icon {
    width: 24px;
    height: 24px;
    background: var(--icon-blue);
    display: flex;
    align-items: center;
    justify-content: center;
  }
  .back-mark {
    position: absolute;
    right: 34px;
    top: 146px;
    display: flex;
    align-items: center;
    gap: 8px;
  }
  .back-mark__dot {
    width: 28px;
    height: 28px;
    border-radius: 50%;
    background: var(--faint-mark);
  }
  .back-mark__name {
    font-size: 15px;
    font-weight: 700;
    color: var(--faint-mark);
  }
</style>
</head>
<body>
  <main class="card-set">
    <section class="card card--front" aria-label="Card front">
      <div class="card__band card__band--top"><span class="band-light"></span><span class="band-dark"></span></div>
      <div class="brand-lockup">
        <div class="brand-lockup__dot"></div>
        <div class="brand-lockup__name">Harbourline<br>Career Partners</div>
      </div>
      <p class="website">harbourlinecareer.com.au</p>
      <div class="card__band card__band--bottom"><span class="band-light"></span><span class="band-dark"></span></div>
    </section>

    <section class="card card--back" aria-label="Card back">
      <div class="card__band card__band--top"><span class="band-light"></span><span class="band-dark"></span></div>
      <div class="person">
        <p class="person__name">Gavin Holloway</p>
        <p class="person__role">OWNER</p>
      </div>
      <ul class="contact-list">
        <li>
          <span class="contact-icon">
            <svg width="14" height="14" viewBox="0 0 24 24" aria-hidden="true"><path fill="#fff" d="M6.6 10.8a15.1 15.1 0 0 0 6.6 6.6l2.2-2.2c.3-.3.7-.4 1-.2 1.1.4 2.3.6 3.6.6.6 0 1 .4 1 1V20c0 .6-.4 1-1 1A17 17 0 0 1 3 4c0-.6.4-1 1-1h3.5c.6 0 1 .4 1 1 0 1.3.2 2.5.6 3.6.1.3 0 .7-.2 1z"/></svg>
          </span>
          0481937145
        </li>
        <li>
          <span class="contact-icon">
            <svg width="14" height="14" viewBox="0 0 24 24" aria-hidden="true"><rect x="3" y="6" width="18" height="12" fill="none" stroke="#fff" stroke-width="2"/><path d="M3 6l9 7 9-7" fill="none" stroke="#fff" stroke-width="2"/></svg>
          </span>
          gavin@hcp.com.au
        </li>
        <li>
          <span class="contact-icon">
            <svg width="14" height="14" viewBox="0 0 24 24" aria-hidden="true"><path fill="#fff" d="M12 2a7 7 0 0 0-7 7c0 5 7 13 7 13s7-8 7-13a7 7 0 0 0-7-7zm0 9.5A2.5 2.5 0 1 1 12 6.5a2.5 2.5 0 0 1 0 5z"/></svg>
          </span>
          58 Pellimore Cres, Wardell Vic 3197
        </li>
      </ul>
      <div class="back-mark">
        <div class="back-mark__dot"></div>
        <div class="back-mark__name">Harbourline</div>
      </div>
      <div class="card__band card__band--bottom"><span class="band-light"></span><span class="band-dark"></span></div>
    </section>
  </main>
</body>
</html>
```